Carewell Hub Needs a Web Design

Designers will use (and improve) our mockups to re-design our mobile-friendly website. We would like to see designs that use the color blue (as our logo in the attached file). The final design should convey convenience and communicate accessible health and wellness.

We need a web design for a company based in Kampala called 'Carewell Hub'.

We help patients to compare health insurance, find a doctor and book an appointment instantly.

Our initial products are Find and Book - a Wordpress database that helps patients to find a doctor and book an appointment instantly; and Insurance - a database that helps patients compare health insurance policies online. We would like to see designs that are mobile-friendly and responsive with awesome user interface and experience.
Updates

Project Deadline Extended Reason: We need web design of 5+ pages. Please see attached files for guidance. Added Wednesday, February 17, 2016

Industry/Entity Type

Health Service

Number of Pages Required

5+ page

Font styles to use
Sans Serif

Colors
33a6d7
85cae6
cee9f5
ecf7fb

Requirements
Must have
• Mobile-friendly and responsive design with awesome UI and UX

```html
<!DOCTYPE html>
<html lang="en">
<head>
<meta charset="utf-8">
<title>Carewell Hub</title>
<link href="https://fonts.googleapis.com/css2?family=Raleway:wght@400;500;600&display=swap" rel="stylesheet">
<style>
:root{
  --blue:#33a6d7;
  --blue-bright:#25b3e8;
  --blue-soft:#85cae6;
  --ink:#222;
  --muted:#555;
  --white:#fff;
  --grey-band:#e9e9e9;
  --footer:#2b2b2b;
}
*{margin:0;padding:0;box-sizing:border-box}
html,body{width:1200px;height:2590px;overflow:hidden}
body{font-family:'Raleway',sans-serif;color:var(--ink);background:var(--white);position:relative}
.abs{position:absolute}
section,header,footer{position:absolute;left:0;width:1200px;overflow:hidden}

/* header */
.site-header{top:0;height:90px;background:var(--white)}
.nav-link{font-size:16px;color:var(--ink);top:37px}
.brand{left:500px;top:30px;display:flex;align-items:center;gap:10px;font-size:21px;font-weight:600;color:var(--ink)}
.brand-mark{width:22px;height:22px;border-radius:50%;background:var(--blue)}
.btn-top{top:33px;height:33px;font-size:13px;display:flex;align-items:center;justify-content:center;border:2px solid #bbb;color:var(--ink)}
.btn-top.primary{background:var(--blue-bright);border-color:var(--blue-bright);color:var(--white)}

/* hero */
.hero{top:90px;height:563px}
.hero-photo{position:absolute;inset:0;background:linear-gradient(110deg,#6b6b6b 0%,#8d8a86 35%,#a7a39e 60%,#7c7a78 100%)}
.hero-photo::after{content:"";position:absolute;inset:0;background:rgba(0,0,0,.22)}
.hero-title{top:50px;width:100%;text-align:center;color:var(--white);font-size:44px;font-weight:400}
.search{left:325px;top:117px;width:547px;height:59px;background:var(--blue-bright);padding:6px;display:flex}
.search-field{flex:1;background:var(--white);display:flex;align-items:center;gap:10px;padding-left:14px;font-size:13px;color:#333}
.search-btn{width:60px;display:flex;align-items:center;justify-content:center}
.category{width:160px;text-align:center;color:var(--white);font-size:17px}
.category svg{display:block;margin:0 auto 6px}
.slide-arrow{top:318px;width:76px;height:76px;border-radius:50%;background:#222;display:flex;align-items:center;justify-content:center}

/* app */
.app{top:653px;height:378px;background:var(--white)}
.app-devices{left:173px;top:52px;width:310px;height:326px;background:linear-gradient(160deg,#f1f3f5,#cfd6dc);border-radius:18px 18px 0 0}
.app-title{left:530px;top:96px;font-size:31px;font-weight:400;line-height:1.3}
.app-title span{display:block;color:var(--blue-bright);font-size:26px}
.app-text{left:530px;top:188px;width:480px;font-size:11.5px;line-height:22px;color:var(--muted)}
.store-badge{top:269px;height:40px;background:#111;border-radius:5px}

/* shared band headings */
.band-title{font-size:24px;font-weight:400}
.band-rule{height:1px}
.feature{display:flex;align-items:center;gap:12px;font-size:18px}
.feature-icon{width:50px;height:50px;border-radius:50%;border:2px solid currentColor;display:flex;align-items:center;justify-content:center}
.btn-outline{height:43px;display:flex;align-items:center;justify-content:center;font-size:17px;border:2px solid currentColor}

/* money */
.money{top:1031px;height:487px;color:var(--white)}
.money-photo{position:absolute;inset:0;background:linear-gradient(120deg,#3b4a55,#56636c 50%,#3d4a54)}
.money-photo::after{content:"";position:absolute;inset:0;background:rgba(20,30,40,.45)}
.offer{left:805px;top:167px;width:214px;height:214px;border-radius:50%;background:var(--blue-bright);box-shadow:0 0 0 5px var(--white) inset,0 0 0 10px var(--blue-bright) inset;display:flex;align-items:center;justify-content:center;text-align:center;font-size:18px;line-height:31px;padding:30px}

/* worry */
.worry{top:1518px;height:473px;background:var(--grey-band)}
.step{width:240px;text-align:center;font-size:14px;line-height:18px;color:#333}
.step-icon{width:80px;height:80px;border-radius:50%;background:var(--blue-bright);display:flex;align-items:center;justify-content:center;margin:0 auto 20px}

/* time */
.time{top:1991px;height:487px;background:var(--blue-bright);color:var(--white)}
.time-phone{left:843px;top:162px;width:129px;height:259px;border-radius:18px;background:linear-gradient(180deg,#f5f7f9,#dfe5ea)}

/* footer */
.site-footer{top:2478px;height:112px;background:var(--footer);color:var(--white)}
.foot-link{top:26px;font-size:15px}
.copyright{left:181px;top:57px;font-size:11px}
.social{top:18px;width:27px;height:27px;border-radius:50%;border:2px solid var(--white)}
</style>
</head>
<body>

<header class="site-header">
  <a class="abs nav-link" style="left:197px">CWH for Doctors</a>
  <a class="abs nav-link" style="left:353px">Blog</a>
  <div class="abs brand"><span class="brand-mark"></span>Carewell Hub</div>
  <a class="abs btn-top primary" style="left:722px;width:109px">Insurance</a>
  <a class="abs btn-top" style="left:839px;width:87px">Login</a>
  <a class="abs btn-top" style="left:932px;width:87px">Register</a>
</header>

<section class="hero">
  <div class="hero-photo" role="img" aria-label="Photo of a family visiting a doctor"></div>
  <h1 class="abs hero-title">Find and Book</h1>
  <div class="abs search">
    <div class="search-field">
      <svg width="20" height="20" viewBox="0 0 20 20"><circle cx="8" cy="8" r="6" fill="none" stroke="#999" stroke-width="2"/><line x1="12.5" y1="12.5" x2="18" y2="18" stroke="#999" stroke-width="2.4"/></svg>
      Specialist, Doctors, Clinics, Hospitals, Tests, Etc
    </div>
    <div class="search-btn"><svg width="24" height="24" viewBox="0 0 20 20"><circle cx="8" cy="8" r="6" fill="none" stroke="#fff" stroke-width="2.5"/><line x1="12.5" y1="12.5" x2="18" y2="18" stroke="#fff" stroke-width="3"/></svg></div>
  </div>

  <div class="abs category" style="left:257px;top:250px"><svg width="40" height="44" viewBox="0 0 40 44"><circle cx="20" cy="11" r="9" fill="#fff"/><path d="M4 44v-8c0-8 7-13 16-13s16 5 16 13v8z" fill="#fff"/></svg>Doctors</div>
  <div class="abs category" style="left:416px;top:250px"><svg width="40" height="44" viewBox="0 0 40 44"><path d="M14 4h12v12l10 24H4l10-24z" fill="#fff"/></svg>Lab Tests</div>
  <div class="abs category" style="left:576px;top:250px"><svg width="40" height="44" viewBox="0 0 40 44"><path d="M6 8c0-6 10-6 14-3 4-3 14-3 14 3 0 8-3 12-4 20-1 8-5 8-6 0-1-4-3-4-4 0-1 8-5 8-6 0-1-8-8-12-8-20z" fill="#fff"/></svg>Dentist</div>
  <div class="abs category" style="left:737px;top:246px"><svg width="40" height="44" viewBox="0 0 40 44"><circle cx="20" cy="18" r="14" fill="none" stroke="#fff" stroke-width="2.5"/><path d="M14 32v10h12V32" fill="none" stroke="#fff" stroke-width="2.5"/></svg>Dermatologist</div>
  <div class="abs category" style="left:338px;top:357px"><svg width="40" height="44" viewBox="0 0 40 44"><path d="M20 42C4 30 2 22 2 15 2 7 8 3 13 3c4 0 6 2 7 5 1-3 3-5 7-5 5 0 11 4 11 12 0 7-2 15-18 27z" fill="#fff"/></svg>Cardiologist</div>
  <div class="abs category" style="left:516px;top:357px"><svg width="40" height="44" viewBox="0 0 40 44"><path d="M10 42V30C4 26 4 18 6 12 9 4 18 2 24 4c8 3 10 10 9 16l4 6h-4v8h-8v8" fill="none" stroke="#fff" stroke-width="2.5"/></svg>Ear Nose Throat</div>
  <div class="abs category" style="left:692px;top:357px"><svg width="40" height="44" viewBox="0 0 40 44"><ellipse cx="20" cy="20" rx="17" ry="13" fill="none" stroke="#fff" stroke-width="2.5"/><path d="M20 8v24M10 14c4 2 4 8 0 10M30 14c-4 2-4 8 0 10" fill="none" stroke="#fff" stroke-width="2"/></svg>Phychiatrist</div>

  <div class="abs slide-arrow" style="left:-38px"><svg width="30" height="30" viewBox="0 0 30 30" style="margin-left:34px"><path d="M18 7l-8 8 8 8" fill="none" stroke="#fff" stroke-width="3"/></svg></div>
  <div class="abs slide-arrow" style="left:1162px"><svg width="30" height="30" viewBox="0 0 30 30" style="margin-right:34px"><path d="M12 7l8 8-8 8" fill="none" stroke="#fff" stroke-width="3"/></svg></div>
</section>

<section class="app">
  <div class="abs app-devices" role="img" aria-label="Two smartphones showing the doctor booking app"></div>
  <h2 class="abs app-title">Find a Doctor and book an<span>appointment in Seconds!</span></h2>
  <p class="abs app-text">Ut nisi erat fermentum vel congue id euismod in elit Fusce ultricies orci ac feugiat suscipit leo massa sodales velit et scelerisque mi tortor at ipsum cligula augue bibendum accumsan vestibulum ut commodo a mi Morbi ornare gravida elit</p>
  <div class="abs store-badge" style="left:530px;width:123px" role="img" aria-label="App store download badge"></div>
  <div class="abs store-badge" style="left:660px;width:136px" role="img" aria-label="App store download badge"></div>
</section>

<section class="money">
  <div class="money-photo" role="img" aria-label="Photo of a smiling medical team"></div>
  <h2 class="abs band-title" style="left:199px;top:45px">Carewell Hub saves you Money</h2>
  <svg class="abs" style="left:985px;top:36px" width="26" height="46" viewBox="0 0 26 46"><path d="M22 12c-2-4-6-5-9-5-5 0-9 3-9 7 0 10 18 6 18 17 0 4-4 8-9 8-4 0-8-2-10-6M13 2v42" fill="none" stroke="#fff" stroke-width="4"/></svg>
  <div class="abs band-rule" style="left:199px;top:96px;width:833px;background:rgba(255,255,255,.45)"></div>
  <p class="abs" style="left:0;width:1200px;top:119px;text-align:center;font-size:18px">Compare over 8 Health Insurance Providers and get covered today!</p>

  <div class="abs feature" style="left:225px;top:189px"><span class="feature-icon"><svg width="22" height="22" viewBox="0 0 22 22"><rect x="2" y="4" width="15" height="15" rx="2" fill="none" stroke="#fff" stroke-width="2"/><path d="M8 14l1-4 9-9 3 3-9 9z" fill="#fff"/></svg></span>Get a free, no obligation health insurance quote</div>
  <div class="abs feature" style="left:225px;top:251px"><span class="feature-icon"><svg width="24" height="24" viewBox="0 0 24 24"><circle cx="12" cy="12" r="10" fill="none" stroke="#fff" stroke-width="2"/><circle cx="8.5" cy="9.5" r="1.4" fill="#fff"/><circle cx="15.5" cy="9.5" r="1.4" fill="#fff"/><path d="M7 14c2 4 8 4 10 0" fill="none" stroke="#fff" stroke-width="2"/></svg></span>Simple and Jargon free</div>
  <div class="abs feature" style="left:225px;top:311px"><span class="feature-icon"><svg width="24" height="20" viewBox="0 0 24 20"><rect x="1" y="3" width="22" height="14" rx="2" fill="none" stroke="#fff" stroke-width="2"/><circle cx="12" cy="10" r="3.5" fill="#fff"/></svg></span>Low Monthly Payments</div>

  <div class="abs offer">Take care of your loved onces from UGX 30,000 A Month!</div>
  <a class="abs btn-outline" style="left:487px;top:399px;width:261px">Compare Now</a>
</section>

<section class="worry">
  <h2 class="abs band-title" style="left:174px;top:32px">Carewell Hub saves you worry</h2>
  <svg class="abs" style="left:940px;top:22px" width="52" height="52" viewBox="0 0 52 52"><path d="M10 50V14h32v36M4 50h44" fill="none" stroke="#222" stroke-width="2.5"/><circle cx="26" cy="10" r="8" fill="#fff" stroke="#222" stroke-width="2.5"/><path d="M26 5v10M21 10h10" stroke="#222" stroke-width="2.5"/><path d="M16 22h4M24 22h4M32 22h4M16 30h4M24 30h4M32 30h4M16 38h4M32 38h4M23 50V40h6v10" stroke="#222" stroke-width="2.5" fill="none"/></svg>
  <div class="abs band-rule" style="left:173px;top:82px;width:835px;background:#bbb"></div>
  <p class="abs" style="left:0;width:1200px;top:116px;text-align:center;font-size:15px;line-height:22px;color:#444">Worry. It never feels good. We'd rather you experience more enjoybale emotions<br>like happiness. Raise funds for your medical cause</p>

  <div class="abs step" style="left:193px;top:213px"><div class="step-icon"><svg width="34" height="34" viewBox="0 0 22 22"><rect x="2" y="4" width="15" height="15" rx="2" fill="none" stroke="#fff" stroke-width="1.8"/><path d="M8 14l1-4 9-9 3 3-9 9z" fill="#fff"/></svg></div>Create a campaign to raise<br>funds for your medical cause.</div>
  <div class="abs step" style="left:438px;top:213px"><div class="step-icon"><svg width="34" height="26" viewBox="0 0 34 26"><rect x="2" y="2" width="30" height="22" rx="3" fill="none" stroke="#fff" stroke-width="2.5"/><rect x="2" y="8" width="30" height="4" fill="#fff"/><rect x="6" y="17" width="8" height="2.5" fill="#fff"/></svg></div>Recieve dontation to your<br>cause direct to your account</div>
  <div class="abs step" style="left:736px;top:213px"><div class="step-icon"><svg width="32" height="32" viewBox="0 0 32 32"><rect x="3" y="10" width="26" height="7" fill="#fff"/><rect x="5" y="17" width="22" height="13" fill="#fff"/><rect x="14.5" y="10" width="3" height="20" fill="#25b3e8"/><path d="M16 10c-3-7-10-7-9-2 1 3 6 2 9 2 3 0 8 1 9-2 1-5-6-5-9 2" fill="none" stroke="#fff" stroke-width="2"/></svg></div>Support any cause or<br>campaign your like</div>

  <div class="abs" style="left:706px;top:212px;width:1px;height:230px;background:#c4c4c4"></div>
  <a class="abs btn-outline" style="left:338px;top:376px;width:190px;height:38px;font-size:14px;color:#222">Start a campaign</a>
  <a class="abs btn-outline" style="left:768px;top:376px;width:190px;height:38px;font-size:14px;color:#222">Donate</a>
</section>

<section class="time">
  <h2 class="abs band-title" style="left:185px;top:43px">Carewell Hub saves you time</h2>
  <svg class="abs" style="left:952px;top:33px" width="42" height="42" viewBox="0 0 42 42"><rect x="2" y="6" width="38" height="34" rx="3" fill="none" stroke="#fff" stroke-width="2.5"/><rect x="2" y="6" width="38" height="8" fill="#fff"/><path d="M11 2v8M31 2v8" stroke="#fff" stroke-width="3"/><path d="M9 20h5M18 20h5M27 20h5M9 27h5M18 27h5M27 27h5M9 34h5M18 34h5" stroke="#fff" stroke-width="3"/></svg>
  <div class="abs band-rule" style="left:183px;top:97px;width:834px;background:rgba(255,255,255,.55)"></div>
  <p class="abs" style="left:0;width:1200px;top:120px;text-align:center;font-size:18px">We know you didn't want to send all your time waiting in line</p>

  <div class="abs feature" style="left:211px;top:168px"><span class="feature-icon"><svg width="22" height="22" viewBox="0 0 22 22"><rect x="2" y="4" width="18" height="16" rx="2" fill="none" stroke="#fff" stroke-width="2"/><path d="M7 12l3 3 6-6M7 1v5M15 1v5" fill="none" stroke="#fff" stroke-width="2"/></svg></span>See doctor's schedule</div>
  <div class="abs feature" style="left:211px;top:229px"><span class="feature-icon"><svg width="24" height="24" viewBox="0 0 24 24"><circle cx="12" cy="12" r="9" fill="none" stroke="#fff" stroke-width="2"/><path d="M12 6v6l4 3" fill="none" stroke="#fff" stroke-width="2"/></svg></span>Choose a time that works for you</div>
  <div class="abs feature" style="left:211px;top:291px"><span class="feature-icon"><svg width="24" height="24" viewBox="0 0 24 24"><circle cx="12" cy="12" r="10" fill="#fff"/><path d="M7 12l4 4 6-7" fill="none" stroke="#25b3e8" stroke-width="2.5"/></svg></span>Book instantly. No phone calls. No waiting on hold</div>

  <div class="abs time-phone" role="img" aria-label="Smartphone showing the appointment booking screen"></div>
  <a class="abs btn-outline" style="left:471px;top:399px;width:261px">Book an appointment now</a>
</section>

<footer class="site-footer">
  <a class="abs foot-link" style="left:181px">About</a>
  <a class="abs foot-link" style="left:247px">Contact Us</a>
  <a class="abs foot-link" style="left:345px">Privacy &amp; Terms</a>
  <p class="abs copyright">© 2016 Company Name &nbsp;All right reserved &nbsp;Term of Use</p>
  <span class="abs social" style="left:902px"></span>
  <span class="abs social" style="left:932px"></span>
  <span class="abs social" style="left:962px"></span>
  <span class="abs social" style="left:992px"></span>
</footer>

</body>
</html>
```